FLYER für Fortbildung
Zielgruppe
Die Fortbildung, die beworben werden soll, richtet sich an Fachkräfte, die in Kitas arbeiten. In diesem Fall handelt es sich um eine praxisorientierte Online-Live-Fortbildung - dies bedeutet, die TeilnehmerInnen werden während der Online-Fortbildung kontinuierlich durch eine Referentin begleitet. Die Fortbildung erweitert das Wissen und die Kompetenzen der Teilnehmenden.
Aufgabenstellung
Ich freue mich über Vorschläge eines Falzflyers im Format DIN lang. Wie viele Seiten der Flyer umfasst, überlasse ich gerne Ihnen, da dies von Ihrer Gestaltung abhängt.
Falls Sie 1-4 Bilder einfügen möchten, gebe ich Ihnen in den Datei-Upload gerne einige Beispiele, die mir zusagen (zur Auswahl). Darüber hinaus bin ich selbstverständlich auch offen für alternative Vorschläge sowie neue Designs.

```html
<!DOCTYPE html>
<html lang="de">
<head>
<meta charset="utf-8">
<title>Elterngespräche führen – Flyer</title>
<link href="https://fonts.googleapis.com/css2?family=Lato:ital,wght@0,400;0,700;0,900;1,400&display=swap" rel="stylesheet">
<style>
:root{
  --bg:#dcdcdc;
  --light:#c3cbdc;
  --mid:#6f81a0;
  --ink:#2f3033;
  --white:#ffffff;
  --form:#dfe3ec;
  --accent:#6f81a0;
}
*{box-sizing:border-box;margin:0;padding:0}
html,body{width:1200px;height:1091px;overflow:hidden;background:var(--bg);font-family:'Lato',sans-serif;color:var(--ink)}
.canvas{position:relative;width:1200px;height:1091px}
.page{position:absolute;overflow:hidden;box-shadow:4px 6px 12px rgba(0,0,0,.22);background:var(--white)}
.band{position:absolute;left:0;right:0}
.band--light{background:var(--light)}
.band--mid{background:var(--mid)}
.photo{position:absolute}
.photo--family{background:linear-gradient(135deg,#efe9e3 0%,#d9cfc6 45%,#b7aea8 100%)}
.photo--office{background:linear-gradient(120deg,#c8d3dc 0%,#efefef 40%,#d8d0c8 70%,#8b95a0 100%)}
.photo--consult{background:linear-gradient(120deg,#9fb3c4 0%,#d7d2cc 50%,#6c7684 100%)}
.photo--plants{background:linear-gradient(120deg,#d6c3a1 0%,#9fb48a 50%,#e4e2dc 100%)}
.title{font-weight:900;text-transform:uppercase;text-align:center;letter-spacing:.5px;line-height:1.1;color:var(--ink)}
.subtitle{color:var(--white);font-weight:400;text-align:center}
.fee{position:absolute;background:var(--mid);color:var(--white);font-size:12px;line-height:1.1;padding:3px 8px}
.brand{position:absolute;display:flex;align-items:center;gap:6px;color:var(--mid);font-size:9px;font-weight:400;letter-spacing:.3px}
.brand__dot{width:14px;height:14px;border-radius:50%;border:1.5px solid var(--mid)}
.event{position:absolute;font-size:14px;line-height:1.3;color:var(--ink)}
.address{position:absolute;color:var(--white);font-size:10px;line-height:1.25}
.address strong{font-weight:400;font-size:11px;letter-spacing:.3px}
.contact{position:absolute;color:var(--mid);font-size:9px;line-height:1.3}
.inside{background:var(--mid);color:var(--white)}
.inside p{font-size:8.5px;line-height:1.4}
.contents h3{font-size:11px;font-weight:700;margin-bottom:8px}
.contents ul{list-style:none}
.contents li{display:flex;align-items:center;gap:7px;font-size:8.5px;margin-bottom:7px}
.form{position:absolute;background:var(--form);color:var(--ink);padding:10px 12px}
.form__date{font-size:9px;margin-bottom:12px}
.form__field{font-size:6px;border-bottom:.6px solid var(--ink);height:26px;padding-top:2px}
.form__sign{display:flex;justify-content:space-between;font-size:6px;padding-top:2px;border-top:.6px solid var(--ink);margin-top:12px}
.fineprint{position:absolute;font-size:5.5px;line-height:1.35;color:var(--white)}
</style>
</head>
<body>
<div class="canvas">

  <!-- Cover -->
  <section class="page page--cover" style="left:40px;top:30px;width:300px;height:520px">
    <div class="band band--light" style="top:0;height:150px"></div>
    <h1 class="title" style="position:absolute;top:48px;left:0;right:0;font-size:24px">Elterngespräche<br>führen</h1>
    <div class="photo photo--family" role="img" aria-label="Foto: lächelnde Familie mit Tochter auf einem Sofa im Gespräch" style="top:150px;left:10px;right:10px;height:220px"></div>
    <div class="fee" style="top:315px;right:22px">Teilnahmegebühr:<br>99,00 € pro Person</div>
    <div class="band band--light" style="top:370px;height:40px"></div>
    <div class="band band--mid" style="top:398px;height:74px"></div>
    <div class="subtitle" style="position:absolute;top:412px;left:0;right:0;font-size:34px">Grundlagen</div>
    <div class="brand" style="right:20px;bottom:14px"><span class="brand__dot"></span>GUTE WEGE IM BERUF</div>
  </section>

  <!-- Inside spread -->
  <section class="page inside" style="left:560px;top:30px;width:540px;height:500px">
    <div class="photo photo--consult" role="img" aria-label="Foto: Fachkraft im Beratungsgespräch am Tisch" style="top:0;left:0;width:258px;height:150px"></div>
    <p style="position:absolute;top:160px;left:14px;width:236px;text-align:justify">Diese Fortbildung richtet sich an Berufsanfänger, unsichere Fachkräfte und alle, die ihre Kenntnisse bezüglich Elterngesprächen auffrischen möchten. Ziel ist es, Ihnen Sicherheit und Selbstvertrauen im Umgang mit Eltern zu geben.</p>
    <p style="position:absolute;top:222px;left:14px;width:236px">Benötigt wird ein PC oder Laptop mit Webcam/Mikrofon.</p>
    <div class="contents" style="position:absolute;top:262px;left:14px;width:236px">
      <h3 style="padding-left:16px">Inhalte der Fortbildung:</h3>
      <ul>
        <li><svg width="9" height="10" viewBox="0 0 9 10"><path d="M1 6 L3.5 9 L8 1" stroke="#fff" stroke-width="1.6" fill="none"/></svg>Theoretische Modelle der Gesprächsführung</li>
        <li><svg width="9" height="10" viewBox="0 0 9 10"><path d="M1 6 L3.5 9 L8 1" stroke="#fff" stroke-width="1.6" fill="none"/></svg>Effektive Vorbereitung auf Elterngespräche</li>
        <li><svg width="9" height="10" viewBox="0 0 9 10"><path d="M1 6 L3.5 9 L8 1" stroke="#fff" stroke-width="1.6" fill="none"/></svg>Gesprächseinstieg</li>
        <li><svg width="9" height="10" viewBox="0 0 9 10"><path d="M1 6 L3.5 9 L8 1" stroke="#fff" stroke-width="1.6" fill="none"/></svg>Umgang mit schwierigen Gesprächssituationen</li>
        <li><svg width="9" height="10" viewBox="0 0 9 10"><path d="M1 6 L3.5 9 L8 1" stroke="#fff" stroke-width="1.6" fill="none"/></svg>Deeskalation / Konfliktlösungsstrategien</li>
        <li><svg width="9" height="10" viewBox="0 0 9 10"><path d="M1 6 L3.5 9 L8 1" stroke="#fff" stroke-width="1.6" fill="none"/></svg>Möglichkeiten zum Üben und Austausch</li>
      </ul>
    </div>
    <h2 style="position:absolute;top:18px;left:272px;width:256px;text-align:center;font-size:13px;font-weight:700">ANMELDUNG ZUR FORTBILDUNG</h2>
    <div style="position:absolute;top:36px;left:272px;width:256px;text-align:center;font-size:11px">Elterngespräche führen – Grundlagen</div>
    <p style="position:absolute;top:62px;left:276px;width:250px;font-style:italic;text-align:center">Bitte füllen Sie das Formular aus und senden Sie es an info@gute-wege-beruf.de. Mit Ihrer Anmeldung akzeptieren Sie die aufgeführten Bedingungen*</p>
    <div class="form" style="top:110px;left:276px;width:250px;height:200px">
      <div class="form__date">30. März 2025 von 09:00 – 15:00 Uhr (online)</div>
      <div class="form__field">Vor- und Zuname:</div>
      <div class="form__field">Rechnungsadresse:</div>
      <div class="form__field"></div>
      <div class="form__field">Ihre E-Mail-Adresse für den Zugangslink:</div>
      <div class="form__sign"><span>Ort, Datum</span><span style="margin-right:60px">Unterschrift</span></div>
    </div>
    <div class="photo photo--plants" role="img" aria-label="Foto: Beraterin mit Tablet im Gespräch zwischen Pflanzen" style="top:322px;left:286px;width:240px;height:100px"></div>
    <p class="fineprint" style="top:432px;left:20px;width:505px">*Datenschutz und Teilnahmebedingungen: Nach Eingang Ihrer Anmeldung erhalten Sie eine Bestätigung mit allen Zahlungsangaben. Die Gebühr ist innerhalb von 30 Tagen nach Rechnungsstellung fällig. Ein kostenfreier Rücktritt ist bis vier Wochen vor Beginn per E-Mail möglich. Alle Unterlagen sind nur für den persönlichen Gebrauch bestimmt. Ihre Daten werden ausschließlich zur Durchführung der Fortbildung genutzt und nicht an Dritte weitergegeben. Sie können Ihre Zustimmung jederzeit widerrufen.</p>
  </section>

  <!-- Back page -->
  <section class="page page--back" style="left:260px;top:560px;width:270px;height:510px">
    <div class="band band--light" style="top:0;height:110px"></div>
    <div class="event" style="top:16px;left:28px">| Live-Online-Fortbildung für<br>&nbsp;&nbsp;Mitarbeitende in Kitas<br>| Montag, den 30. März 2026<br>| 09:00 bis 15:00 Uhr</div>
    <div class="photo photo--office" role="img" aria-label="Foto: lächelnde Frau am Schreibtisch vor einem Fenster" style="top:110px;left:0;width:250px;height:220px"></div>
    <div class="band band--mid" style="top:110px;left:250px;width:20px;height:220px"></div>
    <div class="band band--light" style="top:330px;height:40px"></div>
    <div class="band band--mid" style="top:370px;height:80px"></div>
    <div class="address" style="top:384px;left:40px"><strong>GUTE WEGE IM BERUF</strong><br>Helene Brandt<br>Lindenweg 8<br>67433 Talheim</div>
    <div class="contact" style="top:462px;left:40px">Telefon: +49 151 23487651<br>E-Mail: kontakt@gute-wege-beruf.de<br>Homepage: www.gute-wege-beruf.de</div>
  </section>

  <!-- Outer spread -->
  <section class="page page--outer" style="left:630px;top:560px;width:530px;height:500px">
    <div class="band band--light" style="top:0;height:120px"></div>
    <div class="event" style="top:18px;left:30px">| Live-Online-Fortbildung für<br>&nbsp;&nbsp;Mitarbeitende in Kitas<br>| Montag, den 30. März 2026<br>| 09:00 bis 15:00 Uhr</div>
    <h1 class="title" style="position:absolute;top:40px;left:280px;width:240px;font-size:22px">Elterngespräche<br>führen</h1>
    <div class="photo photo--office" role="img" aria-label="Foto: lächelnde Frau am Schreibtisch vor einem Fenster" style="top:120px;left:10px;width:245px;height:210px"></div>
    <div class="band band--mid" style="top:120px;left:255px;width:16px;height:210px"></div>
    <div class="photo photo--family" role="img" aria-label="Foto: lächelnde Familie mit Tochter auf einem Sofa im Gespräch" style="top:120px;left:271px;width:250px;height:210px"></div>
    <div class="fee" style="top:270px;right:14px">Teilnahmegebühr:<br>99,00 € pro Person</div>
    <div class="band band--light" style="top:330px;height:30px"></div>
    <div class="band band--mid" style="top:345px;height:75px"></div>
    <div class="address" style="top:358px;left:40px"><strong>GUTE WEGE IM BERUF</strong><br>Helene Brandt<br>Lindenweg 8<br>67433 Talheim</div>
    <div class="subtitle" style="position:absolute;top:366px;left:280px;width:240px;font-size:32px">Grundlagen</div>
    <div class="contact" style="top:432px;left:40px">Telefon: +49 151 23487651<br>E-Mail: kontakt@gute-wege-beruf.de<br>Homepage: www.gute-wege-beruf.de</div>
    <div class="brand" style="right:20px;bottom:18px"><span class="brand__dot"></span>GUTE WEGE IM BERUF</div>
  </section>

</div>
</body>
</html>
```